【依頼の目的/概要】
電子書籍(bookrie)の表紙デザインをお願いします。

【画像サイズ】※BRPより抜粋
表紙ファイルの理想的な寸法は2,560×1,600ピクセルです。
注:画像の寸法は10,000×10,000ピクセルです。

【タイトル】
資格試験 ゴールダッシュ・速習・楽々学習術

サブタイトル
通れる学び方

【著者】
行政書士 社会保険労務士
森川澄江

【本の内容】
行政書士試験の勉強を短期間で仕上げて、合格する勉強法を
書いた本です。

【デザイン要望】
特にこだわりません。
素敵なデザインの応募を楽しみにしています。
※次点、次々点の方への参加報酬を設定しました。

その他
必要な情報がありましたらお問い合わせください。

本を以下に添付します。
本文中にエクセルで作成した表を挿入します。

明るく見やすく、わかり易い表現が良かったです。

皆様お疲れ様でした。
T_okabe様には訂正を速攻して頂きありがとうございました。
最後まで迷いました。
皆様のご依頼が増えますことをご祈念申し上げます。

```html
<!DOCTYPE html>
<html lang="ja">
<head>
<meta charset="utf-8">
<title>資格試験 ゴールダッシュ 速習・楽々学習術</title>
<link rel="stylesheet" href="https://fonts.googleapis.com/css2?family=Noto+Sans+JP:wght@700;900&family=Noto+Serif+JP:wght@700&display=swap">
<style>
  :root {
    --title-blue: #1c6fc6;
    --ink: #141414;
    --accent-red: #d9262b;
    --band-brown: #3b2418;
    --gold: #c99a2e;
    --paper: #ffffff;
    --sky-top: #8fa6bb;
    --sky-mid: #c9d3dc;
    --road: #4a4642;
  }
  html, body {
    margin: 0;
    padding: 0;
    width: 846px;
    height: 1200px;
    overflow: hidden;
    background: var(--paper);
  }
  .page {
    position: relative;
    width: 846px;
    height: 1200px;
    background: var(--paper);
  }
  .cover {
    position: absolute;
    left: 133px; top: 71px;
    width: 595px; height: 1066px;
    overflow: hidden;
    background: var(--paper);
    font-family: "Noto Sans JP", sans-serif;
    color: var(--ink);
  }
  .hero-photo {
    position: absolute;
    left: 0; top: 0;
    width: 595px; height: 480px;
    background: linear-gradient(180deg, var(--sky-top) 0%, var(--sky-mid) 35%, #e8ecef 50%, #8a8580 64%, var(--road) 80%, #ffffff 100%);
  }
  .seal-mark {
    position: absolute;
    left: 37px; top: 29px;
    width: 185px; height: 243px;
    background: radial-gradient(ellipse at center, rgba(226,170,160,0.55) 0%, rgba(226,170,160,0.15) 60%, rgba(226,170,160,0) 75%);
  }
  .title-main {
    position: absolute;
    left: 0; top: 392px;
    width: 595px;
    margin: 0;
    text-align: center;
    font-weight: 900;
    font-size: 98px;
    line-height: 1;
    letter-spacing: 2px;
    color: var(--title-blue);
    text-shadow:
      4px 0 0 #fff, -4px 0 0 #fff, 0 4px 0 #fff, 0 -4px 0 #fff,
      3px 3px 0 #fff, -3px -3px 0 #fff, 3px -3px 0 #fff, -3px 3px 0 #fff;
  }
  .title-sub {
    position: absolute;
    left: 0; top: 500px;
    width: 595px;
    text-align: center;
    font-weight: 900;
    font-size: 60px;
    line-height: 1.1;
  }
  .divider-band {
    position: absolute;
    left: 0; top: 660px;
    width: 595px; height: 28px;
    background: var(--band-brown);
  }
  .portrait-photo {
    position: absolute;
    left: 347px; top: 700px;
    width: 248px; height: 366px;
    background: linear-gradient(180deg, #f3efea 0%, #e7dcd1 55%, #d3c3b2 100%);
  }
  .ampersand {
    position: absolute;
    left: 290px; top: 720px;
    font-family: "Noto Serif JP", serif;
    font-weight: 700;
    font-size: 170px;
    line-height: 1;
    color: var(--gold);
    opacity: 0.9;
  }
  .subtitle {
    position: absolute;
    left: 160px; top: 730px;
    margin: 0;
    font-weight: 900;
    font-size: 42px;
    color: var(--accent-red);
  }
  .author {
    position: absolute;
    left: 36px; top: 820px;
    font-weight: 700;
    line-height: 1.4;
  }
  .author-label { font-size: 24px; }
  .author-credential { font-size: 29px; }
  .author-name {
    margin-top: 4px;
    font-size: 40px;
    font-weight: 900;
    letter-spacing: 3px;
  }
</style>
</head>
<body>
  <div class="page">
    <main class="cover">
      <div class="hero-photo" role="img" aria-label="青空の下、道路を駆けていく男性の写真"></div>
      <div class="seal-mark" role="img" aria-label="赤い円の中に合格と押された印影"></div>

      <h1 class="title-main">資格試験</h1>
      <div class="title-sub">
        <div>ゴールダッシュ</div>
        <div>速習・楽々学習術</div>
      </div>

      <div class="divider-band"></div>

      <div class="portrait-photo" role="img" aria-label="指でOKサインを作り微笑むスーツ姿の女性の写真"></div>

      <div class="ampersand" aria-hidden="true">&amp;</div>
      <h2 class="subtitle">通れる学び方</h2>

      <div class="author">
        <div class="author-label">著者</div>
        <div class="author-credential">行政書士</div>
        <div class="author-credential">社会保険労務士</div>
        <div class="author-name">森川 澄江</div>
      </div>
    </main>
  </div>
</body>
</html>
```